Elegant wine label

Looking for a new Napa Valley wine label called "Velmira". Our wines will retail for $150 + per bottle. Velmira is derived from the greek word Ergo (therefore) tied in with Air for aeration for wine.

We handcraft our small production wine. 200 cases.
Looking for a very sophisticated, minimalist elegant look. Wine labels we like for inspiration and reference include: www.trelk.wine, www.plavicwine.com, www.morvinestates.com, www.dunleafywine.com, www.kretavine.com/Wine, https://shop.gavrelwine.com/wine

Colors will include white, black and blue foil (Approx. color: C 94.9, M 83.53, Y 0, K 0). We want a custom-created, minimal greek/roman looking font for lettering.

```html
<!DOCTYPE html>
<html lang="en">
<head>
<meta charset="utf-8">
<title>Velmira — Napa Valley Label</title>
<link rel="stylesheet" href="https://fonts.googleapis.com/css2?family=Cormorant+Garamond:wght@400;500;600&display=swap">
<style>
  :root {
    --paper: #ffffff;
    --label-cream: #f5f3e7;
    --label-black: #110e0b;
    --foil-blue: #23449f;
    --ink-light: #ece8dc;
    --ink-muted: #b9b4a8;
    --rule: #5a5650;
    --figure-ink: #1b1815;
  }
  * { margin: 0; padding: 0; box-sizing: border-box; }
  html, body {
    width: 1200px;
    height: 1200px;
    overflow: hidden;
    background: var(--paper);
  }
  .canvas {
    position: relative;
    width: 1200px;
    height: 1200px;
  }
  .label {
    position: absolute;
    left: 120px;
    top: 97px;
    width: 960px;
    height: 1005px;
    border-radius: 16px;
    overflow: hidden;
    background: var(--label-cream);
  }
  .label__sky {
    position: absolute;
    left: 0; top: 0;
    width: 100%;
    height: 588px;
    background: var(--label-cream);
  }
  .label__ground {
    position: absolute;
    left: 0; top: 588px;
    width: 100%;
    height: 417px;
    background: var(--label-black);
  }
  .label__figure {
    position: absolute;
    left: 513px;
    top: 287px;
    width: 178px;
    height: 301px;
  }
  .wordmark {
    position: absolute;
    left: 273px;
    top: 178px;
    width: 172px;
    font-family: "Cormorant Garamond", serif;
    font-weight: 600;
    font-size: 46px;
    line-height: 54px;
    letter-spacing: 2px;
    text-transform: uppercase;
    color: var(--foil-blue);
    text-align: center;
  }
  .divider {
    position: absolute;
    left: 475px;
    top: 144px;
    width: 1px;
    height: 129px;
    background: var(--rule);
  }
  .appellation {
    position: absolute;
    left: 503px;
    top: 170px;
    font-family: "Cormorant Garamond", serif;
    font-weight: 500;
    font-size: 29px;
    letter-spacing: 1px;
    color: var(--ink-light);
    white-space: nowrap;
  }
  .vintage {
    position: absolute;
    left: 504px;
    top: 214px;
    font-family: "Cormorant Garamond", serif;
    font-weight: 500;
    font-size: 16px;
    letter-spacing: 2.5px;
    color: var(--ink-muted);
    white-space: nowrap;
  }
</style>
</head>
<body>
<main class="canvas">
  <section class="label">
    <div class="label__sky"></div>
    <svg class="label__figure" viewBox="0 0 178 301" role="img" aria-label="Black woodcut-style illustration of a horned ancient warrior standing with a spear">
      <defs>
        <linearGradient id="figureTone" x1="0" y1="0" x2="0" y2="1">
          <stop offset="0" stop-color="#2a2622"/>
          <stop offset="1" stop-color="#141210"/>
        </linearGradient>
      </defs>
      <rect x="0" y="0" width="178" height="301" fill="url(#figureTone)"/>
    </svg>
    <div class="label__ground">
      <div class="wordmark">Velmira</div>
      <div class="divider"></div>
      <div class="appellation">Napa Valley</div>
      <div class="vintage">MMXX111</div>
    </div>
  </section>
</main>
</body>
</html>
```